Super-fantastic-interesting infographic of terribly boring content

-Looking to provide a visually engaging snapshot of the average Canadian investor.
-Help people compare their personal financial situation against the infographic (Average).
-We want viewers to feel engaged and interested in the info presented, not confused and irritated.

Data points to present:

The average Canadian snapshot:
* Average Canadian household Income in 2016: $76,900
* Median Net Worth of Canadian families in 2016: $295,100
* Average annual household expenditures on goods a& services: $62,183
* Median value in principal residence: $349,000
* Highest net annual savings amount (Age 35-44): $10,120
* Number of Canadian families holding a mortgage: 38.4%
* Median Mortgage value of Principal residence: $190,000
* Debt to disposable income ratio average: 172.1
* Total value of all assets held by Canadians in 2016: 12 Trillion dollars
* The principal residence was the single largest asset held (of the 12 Trillion): 32%
* Private pensions was the 2nd largest grouping of assets at 29.2%
* The average borrowing rate for Canadian mortgages: 2.94%
* 74% were fixed rate, 21% were variable and 5% blended.
* 48% of Canadians do not save or invest at all
* 54% of Canadians do not budget regularly
* 1 in 3 Canadians have lost at least 20% in one year
* 51% of Canadians took NO ACTION after losing at least 20% in one year.
* 22% of those people either, hired or fired an advisor

Financial advice landscape:
* # of households in Canada: 13,300,000
* Households with an advisor 5,300,000
* % of households dissatisfied with existing advisor 1,100,000

Target Market(s)

Investors, ages 22-55

Industry/Entity Type

Financial

Font styles to use
Sans Serif

Colors

Designer to choose colors to be used in the design.

Requirements
Must have
• Header: Financial landscape of the average Canadian
Nice to have
• There is a lot of numbers and percentages, find a way to deliver the info using a mix of images, numbers, pictures etc.

```html
<!DOCTYPE html>
<html lang="en">
<head>
<meta charset="utf-8">
<title>Financial Landscape of the Average Canadian</title>
<link href="https://fonts.googleapis.com/css2?family=Montserrat:wght@600;700&family=Source+Sans+3:wght@400;600&display=swap" rel="stylesheet">
<style>
:root{
  --red:#ee4a50;
  --red-deep:#e3262f;
  --blue:#1b9bd7;
  --salmon:#ef3a3a;
  --orange:#f47c2a;
  --green:#2a7d2e;
  --purple:#7d4f9e;
  --teal:#18a095;
  --gold:#f29a1f;
  --ink:#1d1d1d;
  --slate:#6f80c0;
  --peach:#f5a27c;
  --pink:#ef6b6e;
  --sage:#86a66a;
  --white:#ffffff;
}
*{margin:0;padding:0;box-sizing:border-box}
html,body{width:760px;height:1200px;overflow:hidden}
body{background:var(--red);font-family:"Source Sans 3",sans-serif;color:var(--ink);position:relative}
.abs{position:absolute}
.panel{position:absolute;background:var(--white)}
.header-title{font-family:"Montserrat",sans-serif;font-weight:600;color:var(--white);font-size:29px;line-height:1;text-decoration:underline;text-decoration-thickness:2px;text-underline-offset:3px;letter-spacing:.3px}
.flag-box{left:672px;top:0;width:88px;height:88px;background:var(--white)}
.art{position:absolute;border-radius:8px}
.stat-icon{position:absolute;width:116px;height:116px;border-radius:50%}
.stat-label{position:absolute;width:150px;text-align:center;font-size:13px;line-height:1.3}
.stat-value{position:absolute;width:150px;text-align:center;font-size:32px;line-height:1}
.big{font-size:30px;line-height:1}
.small{font-size:13px;line-height:1.3}
.tag{font-family:"Montserrat",sans-serif;font-weight:700;color:var(--white);font-size:15px;text-decoration:underline;text-underline-offset:2px}
.advice-num{position:absolute;width:230px;text-align:center;font-size:32px;color:var(--red-deep);line-height:1}
.advice-label{position:absolute;width:230px;text-align:center;font-size:13px;line-height:1.3}
.brand{font-size:36px;font-weight:600;color:#555a60;letter-spacing:-.5px}
</style>
</head>
<body>

<!-- Header -->
<div class="abs header-title" style="left:14px;top:16px">FINANCIAL LANDSCAPE OF THE</div>
<div class="abs header-title" style="left:300px;top:48px">AVERAGE CANADIAN</div>
<div class="abs flag-box">
  <div class="art" role="img" aria-label="Red maple leaf emblem" style="left:16px;top:10px;width:56px;height:64px;background:var(--red-deep);border-radius:10px"></div>
</div>

<!-- Snapshot row -->
<section class="panel" style="left:0;top:88px;width:760px;height:252px">
  <div class="stat-icon" role="img" aria-label="House with dollar sign icon" style="left:24px;top:26px;background:#4fc0ea;border:4px solid #9edcf4"></div>
  <div class="stat-icon" role="img" aria-label="Stack of coins icon" style="left:174px;top:26px;background:#f48a7a;border:4px solid var(--salmon)"></div>
  <div class="stat-icon" role="img" aria-label="Shopping cart icon" style="left:324px;top:26px;background:#fbc372;border:4px solid #f7a44a"></div>
  <div class="stat-icon" role="img" aria-label="House with coins icon" style="left:474px;top:26px;background:#5aa65a;border:4px solid #3c8a3c"></div>
  <div class="stat-icon" role="img" aria-label="Piggy bank icon" style="left:624px;top:26px;background:#eadcf3;border:4px solid #a57cc4"></div>

  <div class="stat-label" style="left:6px;top:154px">Average Canadian<br>household Income<br>in 2016:</div>
  <div class="stat-label" style="left:156px;top:154px">Median Net Worth<br>of Canadian families<br>in 2016:</div>
  <div class="stat-label" style="left:301px;top:154px;width:160px">Average annual household<br>expenditures on<br>goods &amp; services</div>
  <div class="stat-label" style="left:456px;top:154px">Median value<br>in<br>principal residence</div>
  <div class="stat-label" style="left:606px;top:154px">Highest net annual<br>savings amount<br>(Age 35-44)</div>

  <div class="stat-value" style="left:6px;top:210px;color:var(--blue)">$76,900</div>
  <div class="stat-value" style="left:156px;top:210px;color:var(--salmon)">$295,100</div>
  <div class="stat-value" style="left:306px;top:210px;color:var(--orange)">$62,183</div>
  <div class="stat-value" style="left:456px;top:210px;color:var(--green)">$349,000</div>
  <div class="stat-value" style="left:606px;top:210px;color:var(--purple)">$10,120</div>
</section>

<!-- Mortgage panel -->
<section class="panel" style="left:0;top:356px;width:372px;height:232px">
  <div class="art" role="img" aria-label="Hand holding a house with a dollar sign" style="left:4px;top:28px;width:150px;height:168px;background:linear-gradient(180deg,#f4d9a8,#f6c7a3)"></div>
  <svg class="abs" style="left:0;top:0" width="372" height="232" aria-hidden="true">
    <g stroke="#222" stroke-width="1" fill="#222">
      <line x1="124" y1="68" x2="138" y2="56"/><line x1="138" y1="56" x2="160" y2="56"/><circle cx="160" cy="56" r="3"/>
      <line x1="150" y1="128" x2="160" y2="128"/><circle cx="160" cy="128" r="3"/>
      <line x1="128" y1="170" x2="148" y2="192"/><line x1="148" y1="192" x2="162" y2="192"/><circle cx="162" cy="192" r="3"/>
    </g>
  </svg>
  <div class="abs big" style="left:168px;top:20px;color:var(--red-deep)">38.4%</div>
  <div class="abs small" style="left:170px;top:50px;width:190px">Number of Canadian families<br>holding a mortgage</div>
  <div class="abs big" style="left:164px;top:92px;color:var(--red-deep)">$190,000</div>
  <div class="abs small" style="left:166px;top:122px;width:190px">Median Mortgage value of<br>Principal residence</div>
  <div class="abs big" style="left:162px;top:162px;color:var(--red-deep)">172.1</div>
  <div class="abs small" style="left:166px;top:194px;width:200px">Debt to disposable income ratio<br>average</div>
</section>

<!-- Assets panel -->
<section class="panel" style="left:388px;top:356px;width:372px;height:232px">
  <div class="abs" style="left:8px;top:12px;font-size:28px;color:var(--purple);line-height:1">12 Trillion dollars</div>
  <div class="abs small" style="left:12px;top:40px;width:190px;color:var(--purple)">Total value of all assets held by<br>Canadians in 2016</div>
  <div class="abs big" style="left:12px;top:80px;color:var(--teal)">32%</div>
  <div class="abs small" style="left:12px;top:108px;width:200px;color:var(--teal)">The principal residence was the<br>single largest asset held<br>(of the 12 Trillion)</div>
  <div class="abs big" style="left:12px;top:160px;color:var(--gold)">29.2%</div>
  <div class="abs small" style="left:12px;top:190px;width:220px;color:var(--gold)">Private pensions was the 2nd largest<br>grouping of assets</div>
  <svg class="abs" style="left:212px;top:42px" width="140" height="140" viewBox="0 0 140 140" aria-hidden="true">
    <g transform="rotate(-90 70 70)" fill="none" stroke-width="32">
      <circle cx="70" cy="70" r="52" stroke="#7d4f9e" stroke-dasharray="39 287.7" stroke-dashoffset="0"/>
      <circle cx="70" cy="70" r="52" stroke="#f47c2a" stroke-dasharray="39 287.7" stroke-dashoffset="-40.8"/>
      <circle cx="70" cy="70" r="52" stroke="#ef3a3a" stroke-dasharray="39 287.7" stroke-dashoffset="-81.7"/>
      <circle cx="70" cy="70" r="52" stroke="#c0436f" stroke-dasharray="39 287.7" stroke-dashoffset="-122.5"/>
      <circle cx="70" cy="70" r="52" stroke="#2a7fc0" stroke-dasharray="39 287.7" stroke-dashoffset="-163.4"/>
      <circle cx="70" cy="70" r="52" stroke="#18a095" stroke-dasharray="39 287.7" stroke-dashoffset="-204.2"/>
      <circle cx="70" cy="70" r="52" stroke="#7dbb3a" stroke-dasharray="39 287.7" stroke-dashoffset="-245"/>
      <circle cx="70" cy="70" r="52" stroke="#f4c01e" stroke-dasharray="39 287.7" stroke-dashoffset="-285.9"/>
    </g>
  </svg>
  <div class="art" role="img" aria-label="Key icon at centre of the asset wheel" style="left:262px;top:92px;width:40px;height:40px;border-radius:50%;background:#dcdcdc"></div>
</section>

<!-- Mortgage rate panel -->
<section class="panel" style="left:0;top:602px;width:248px;height:268px">
  <div class="abs small" style="left:84px;top:8px;width:60px;text-align:center;color:var(--pink);line-height:1.05;font-size:14px">5%<br>blended</div>
  <svg class="abs" style="left:56px;top:44px" width="136" height="136" viewBox="0 0 136 136" aria-hidden="true">
    <g transform="rotate(-90 68 68)" fill="none" stroke-width="15">
      <circle cx="68" cy="68" r="58" stroke="#8392c7" stroke-dasharray="269.7 94.7"/>
      <circle cx="68" cy="68" r="58" stroke="#f5a27c" stroke-dasharray="76.5 287.9" stroke-dashoffset="-269.7"/>
      <circle cx="68" cy="68" r="58" stroke="#ef6b6e" stroke-dasharray="18.2 346.2" stroke-dashoffset="-346.2"/>
    </g>
  </svg>
  <div class="art" role="img" aria-label="Hands holding a stack of banknotes" style="left:82px;top:86px;width:84px;height:52px;background:#6e9a56"></div>
  <div class="abs small" style="left:6px;top:76px;color:var(--peach);line-height:1.05;font-size:14px">21%<br>variable</div>
  <div class="abs small" style="left:190px;top:150px;width:54px;text-align:right;color:var(--slate);line-height:1.05;font-size:14px">74%<br>fixed rate</div>
  <div class="abs" style="left:0;width:248px;top:196px;text-align:center;font-size:32px;color:var(--sage);line-height:1">2.94%</div>
  <div class="abs small" style="left:0;width:248px;top:226px;text-align:center">The average borrowing<br>rate for Canadian mortgages</div>
</section>

<!-- Behaviour panel -->
<section class="panel" style="left:260px;top:602px;width:498px;height:268px">
  <div class="abs big" style="left:20px;top:10px;color:var(--red-deep)">54%</div>
  <div class="abs small" style="left:20px;top:40px;width:130px">of Canadians do not<br>budget regularly</div>
  <div class="abs big" style="left:20px;top:86px;color:var(--red-deep)">48%</div>
  <div class="abs small" style="left:20px;top:116px;width:130px">of Canadians do not<br>save or invest at all</div>
  <div class="art" role="img" aria-label="Map of Canada" style="left:136px;top:56px;width:186px;height:130px;background:linear-gradient(135deg,#b7dc7a,#7fbd4a)"></div>
  <div class="art" role="img" aria-label="Three green person figures" style="left:48px;top:168px;width:80px;height:50px;background:#4caf6a;border-radius:4px"></div>
  <div class="abs small" style="left:70px;top:224px">1 in 3</div>
  <div class="abs small" style="left:38px;top:238px">Canadians have lost at least <span style="font-size:30px;color:var(--red-deep);vertical-align:-4px">20%</span> in one year</div>
  <div class="abs big" style="left:348px;top:14px;color:var(--red-deep)">51%</div>
  <div class="abs small" style="left:348px;top:44px;width:145px">of Canadians took<br>NO ACTION<br>after losing at least<br><span style="color:var(--red-deep)">20%</span><br>in one year.</div>
  <div class="abs big" style="left:348px;top:140px;color:var(--red-deep)">22%</div>
  <div class="abs small" style="left:348px;top:172px;width:145px">of those people either,<br>hired or fired an advisor</div>
</section>

<!-- Financial advice landscape -->
<section class="panel" style="left:0;top:888px;width:760px;height:204px">
  <div class="abs" style="left:0;top:6px;width:324px;height:30px;background:var(--red)"></div>
  <div class="abs tag" style="left:10px;top:12px">FINANCIAL ADVICE LANDSCAPE:</div>
  <div class="art" role="img" aria-label="Suburban house illustration" style="left:64px;top:44px;width:176px;height:88px;background:linear-gradient(180deg,#f2dfb6,#d9c28f)"></div>
  <div class="art" role="img" aria-label="Advisor holding a clipboard in front of a house" style="left:284px;top:44px;width:152px;height:98px;background:linear-gradient(180deg,#e9d6ad,#2f3440)"></div>
  <div class="art" role="img" aria-label="Advisor with a thumbs-down gesture" style="left:556px;top:32px;width:120px;height:104px;background:linear-gradient(180deg,#b58a6a,#2f3440)"></div>
  <div class="advice-num" style="left:27px;top:136px">13,300,000</div>
  <div class="advice-label" style="left:27px;top:168px"># of households in Canada</div>
  <div class="advice-num" style="left:253px;top:140px">5,300,000</div>
  <div class="advice-label" style="left:253px;top:172px">Households with an advisor</div>
  <div class="advice-num" style="left:507px;top:140px">1,100,000</div>
  <div class="advice-label" style="left:507px;top:172px">% of households dissatisfied<br>with existing advisor</div>
</section>

<!-- Brand -->
<section class="panel" style="left:0;top:1104px;width:760px;height:84px">
  <div class="abs" style="left:248px;top:16px;width:52px;height:52px;border-radius:50%;background:#2a8fd0"></div>
  <div class="abs brand" style="left:312px;top:18px">NorthLedger</div>
</section>

</body>
</html>
```